Life Coaching Business Card

Please check out my website at www.lorettavanmeer.example. Ideally I would like to use the same colors that I used on the site to match my business cards i.e: pink, green, teal, white
I want the final design to include a picture of me and also to be appealing and eye catching. For the picture I submitted, you can crop it smaller to just have my face (exclude my chest) showing.
Industry/Entity Type
Business
Contact Information for Business Card
Loretta Vanmeer
Transformational Life Coach
web: www.lorettavanmeer.example
email: loretta@lorettavanmeer.example
Phone: 555-318-4072
Look and feel
Each slider illustrates characteristics of the customer's brand and the style your logo design should communicate.

```html
<!DOCTYPE html>
<html lang="en">
<head>
<meta charset="utf-8">
<title>Loretta Vanmeer – Business Card</title>
<link href="https://fonts.googleapis.com/css2?family=Arimo:wght@400;700&family=Tinos:wght@400;700&display=swap" rel="stylesheet">
<style>
  :root {
    --backdrop: #e9e6e1;
    --card-white: #ffffff;
    --card-black: #0b0b0b;
    --pink: #e0208f;
    --pink-light: #f27cc0;
    --green: #86d13c;
    --teal: #1fa7a0;
    --ink: #1a1a1a;
    --text-light: #ffffff;
    --photo-dark: #2c2c2c;
    --photo-light: #9a9a9a;
  }
  * { margin: 0; padding: 0; box-sizing: border-box; }
  html, body {
    width: 1200px; height: 833px; overflow: hidden;
    background: var(--backdrop);
  }
  .card {
    position: absolute; left: 50px; top: 102px;
    width: 1100px; height: 629px;
    background: var(--card-black);
    box-shadow: 0 6px 24px rgba(0,0,0,.25);
    overflow: hidden;
  }
  .card-top {
    position: absolute; left: 0; top: 0; width: 1100px; height: 290px;
    background: var(--card-white);
  }
  .brand-mark { position: absolute; left: 10px; top: 10px; }
  .services {
    position: absolute; left: 308px; top: 44px;
    font-family: "Tinos", serif; font-size: 22px; line-height: 30px;
    color: var(--ink);
    list-style: none;
  }
  .appointments { position: absolute; left: 700px; top: 4px; }
  .phone {
    position: absolute; left: 800px; top: 150px;
    font-family: "Tinos", serif; font-size: 28px; color: var(--ink);
  }
  .divider-stripe {
    position: absolute; left: 0; top: 290px; width: 1100px; height: 22px;
    background: linear-gradient(var(--pink) 0 35%, var(--pink-light) 35% 55%, var(--pink) 55% 100%);
  }
  .tagline {
    position: absolute; left: 33px; top: 322px;
    font-family: "Arimo", sans-serif; font-size: 24px; color: var(--green);
  }
  .name {
    position: absolute; left: 770px; top: 322px;
    font-family: "Arimo", sans-serif; font-size: 30px; color: var(--text-light);
  }
  .website {
    position: absolute; left: 100px; top: 368px;
    font-family: "Arimo", sans-serif; font-size: 38px; color: var(--pink);
  }
  .contact-line {
    position: absolute; left: 200px; top: 414px;
    font-family: "Tinos", serif; font-size: 15px; color: var(--text-light);
  }
  .hours-title {
    position: absolute; left: 33px; top: 450px;
    font-family: "Tinos", serif; font-size: 32px; color: var(--green);
  }
  .hours {
    position: absolute; left: 33px; top: 492px;
    font-family: "Tinos", serif; font-size: 24px; line-height: 30px;
    color: var(--text-light); list-style: none;
  }
  .hours span { display: inline-block; width: 200px; }
  .portrait {
    position: absolute; left: 706px; top: 372px; width: 337px; height: 206px;
    background: linear-gradient(120deg, var(--photo-light), var(--photo-dark) 70%);
  }
  .bottom-band {
    position: absolute; left: 0; top: 584px; width: 1100px; height: 45px;
    background: linear-gradient(var(--pink-light), var(--pink));
  }
</style>
</head>
<body>
  <div class="card">
    <div class="card-top">
      <svg class="brand-mark" width="280" height="200" viewBox="0 0 280 200">
        <defs>
          <path id="brand-arc" d="M 20 160 A 110 110 0 0 1 250 130"/>
        </defs>
        <text font-family="Tinos, serif" font-size="26" fill="#1a1a1a">
          <textPath href="#brand-arc">Transformational Life Coach</textPath>
        </text>
        <circle cx="122" cy="170" r="32" fill="#1fa7a0"/>
      </svg>

      <ul class="services">
        <li>Transformational Coaching Method</li>
        <li>Neuro Linguistic Programming</li>
        <li>Positive Psychology</li>
        <li>Ontological Coaching</li>
      </ul>

      <svg class="appointments" width="400" height="150" viewBox="0 0 400 150">
        <defs>
          <path id="appointments-arc" d="M 40 130 A 190 190 0 0 1 380 140"/>
        </defs>
        <text font-family="Tinos, serif" font-size="26" fill="#1a1a1a">
          <textPath href="#appointments-arc">Questions Or Appointments</textPath>
        </text>
      </svg>
      <p class="phone">555-318-4072</p>
    </div>

    <div class="divider-stripe"></div>

    <p class="tagline">Health, Strength, &amp; Balance For Your Mind And Soul.</p>
    <p class="name">Loretta Vanmeer</p>
    <p class="website">www.lorettavanmeer.example</p>
    <p class="contact-line">Contact Me: loretta@lorettavanmeer.example</p>

    <p class="hours-title">Coaching Hours:</p>
    <ul class="hours">
      <li><span>Monday-Thursday</span>9AM-8PM</li>
      <li><span>Friday</span>9AM-6PM</li>
      <li><span>Saturday- Sunday</span>9AM-4PM</li>
    </ul>

    <div class="portrait" role="img" aria-label="Black and white portrait photo of Loretta Vanmeer"></div>

    <div class="bottom-band" role="img" aria-label="Pink decorative patterned band"></div>
  </div>
</body>
</html>
```